Makeup Artist Requires Business Card design

Hi

I am looking for a business card design to market my makeup artist business. I operate under my own name Mara Veldt and I would like to keep the design of the card very simplistic and chic - something that keeps both my name and profession (makeup artist) the focus of the card. I would like it to be a style that is eyecatching to the reader (i am open to anything unusual) but upmarket.

Target Market(s)

women, magazine/beauty/fashion editors, photographers.

Industry/Entity Type

Business

Requirements
Must have
• Must contain:

Phone number: 0418 372 915
Website: www.maraveldt.com.au
email: contact@maraveldt.com.au

(although you don't need to have prefaced these with the words phone number, website etc :))
Should not have
• I am not looking for anything overly colorful - my preference is to keep the card dark if possible.

```html
<!DOCTYPE html>
<html lang="en">
<head>
<meta charset="utf-8">
<title>Mara Veldt – Make-Up Artist Business Card</title>
<link href="https://fonts.googleapis.com/css2?family=Satisfy&family=Cinzel:wght@500&family=Questrial&display=swap" rel="stylesheet">
<style>
  :root {
    --card-black: #000000;
    --card-edge: #8a8a8a;
    --accent-pink: #ee2f8f;
    --name-blue: #5b8ff0;
    --title-pink: #f08ee0;
    --contact-yellow: #f2ea6e;
    --dot-blue: #2c5de8;
    --dot-yellow: #f2f020;
    --dot-purple: #b04ee2;
    --dot-lavender: #dcdcf2;
    --dot-orange: #f27012;
    --photo-light: #f6f3f2;
    --photo-warm: #d9a58f;
    --photo-rose: #c9587a;
  }
  html, body {
    margin: 0;
    padding: 0;
    width: 1200px;
    height: 797px;
    overflow: hidden;
    background: #ffffff;
  }
  .card {
    position: relative;
    width: 1200px;
    height: 797px;
    box-sizing: border-box;
    border: 1px solid var(--card-edge);
    background: var(--card-black);
    overflow: hidden;
  }
  .side-panel {
    position: absolute;
    left: 0;
    top: 0;
    width: 1200px;
    height: 797px;
  }
  .brand {
    position: absolute;
    left: 500px;
    top: 100px;
    width: 510px;
    text-align: center;
  }
  .brand-name {
    margin: 0;
    font-family: "Satisfy", cursive;
    font-weight: 400;
    font-size: 96px;
    line-height: 1.1;
    color: var(--name-blue);
  }
  .brand-rule {
    display: block;
    width: 470px;
    height: 4px;
    margin: -6px auto 0;
    background: var(--name-blue);
  }
  .brand-role {
    margin: 22px 0 0;
    font-family: "Cinzel", serif;
    font-weight: 500;
    font-size: 44px;
    letter-spacing: 1px;
    line-height: 1;
    color: var(--title-pink);
  }
  .palette {
    position: absolute;
    left: 0;
    top: 0;
  }
  .contact {
    position: absolute;
    left: 459px;
    top: 636px;
    margin: 0;
    padding: 0;
    list-style: none;
    font-family: "Questrial", sans-serif;
    font-size: 26px;
    line-height: 39.5px;
    color: var(--contact-yellow);
  }
</style>
</head>
<body>
  <div class="card">
    <svg class="side-panel" width="1200" height="797" viewBox="0 0 1200 797">
      <defs>
        <linearGradient id="cosmetics-tones" x1="0" y1="0" x2="1" y2="1">
          <stop offset="0" stop-color="var(--photo-warm)"/>
          <stop offset="0.45" stop-color="var(--photo-light)"/>
          <stop offset="1" stop-color="var(--photo-rose)"/>
        </linearGradient>
      </defs>
      <polygon class="cosmetics-photo" role="img"
               aria-label="Photograph of make-up brushes, blush compact, eyeshadow palette, mascara and lipsticks on white"
               points="0,0 292,0 390,797 0,797" fill="url(#cosmetics-tones)"/>
      <polygon class="accent-band" points="292,0 321,0 419,797 390,797" fill="var(--accent-pink)"/>
    </svg>

    <header class="brand">
      <h1 class="brand-name">Mara Veldt</h1>
      <span class="brand-rule"></span>
      <p class="brand-role">Make-Up Artist</p>
    </header>

    <svg class="palette" width="1200" height="797" viewBox="0 0 1200 797" aria-hidden="true">
      <circle cx="642" cy="373" r="13" fill="var(--dot-blue)"/>
      <circle cx="707" cy="373" r="13" fill="var(--dot-yellow)"/>
      <circle cx="764" cy="373" r="13" fill="var(--dot-purple)"/>
      <circle cx="822" cy="373" r="13" fill="var(--dot-lavender)"/>
      <circle cx="881" cy="373" r="13" fill="var(--dot-orange)"/>
    </svg>

    <ul class="contact">
      <li class="contact-phone">Phonenumber:0418 372 915</li>
      <li class="contact-web">Website:www.maraveldt.com.au</li>
      <li class="contact-email">email:contact@maraveldt.com.au</li>
    </ul>
  </div>
</body>
</html>
```